Business Card Design Project

Looking to have a new business card created.

The card needs to be sort of two cards attached in the centre creating a flip card so we can write in the centre.

First side with my information at the director / licensee and then the back side with my assistant's details.

Inside with minimal information, facebook link/sign and then lines to write on.

www.kestrelhomeservices.com.au is my website to show colours and designs that I like.
Updates

Target Market(s)

Property Owners, Property Investors, Tenants, rental clients, Tradesman.

Industry/Entity Type

Business

Requirements
Must have
• Professional & symmetrical.

Am getting pro photos for myself & assistance, so a space for these once received.

```html
<!DOCTYPE html>
<html lang="en">
<head>
<meta charset="utf-8">
<title>Kestrel Home Services – Flip Card</title>
<link rel="stylesheet" href="https://fonts.googleapis.com/css2?family=Lato:wght@300;400;700&family=Roboto+Condensed:wght@700&display=swap">
<style>
  :root{
    --board:#a9a9a9;
    --card:#ffffff;
    --card-edge:#b9cbe0;
    --navy:#1d3b53;
    --ink:#222a30;
    --muted:#3f5566;
    --brand-grey:#8d9aa6;
    --band-dark:#0c1f2b;
    --band-mid:#1f4456;
    --band-light:#9fd0ea;
    --line:#3c556a;
  }
  *{margin:0;padding:0;box-sizing:border-box}
  html,body{width:1200px;height:765px;overflow:hidden}
  body{background:var(--board);position:relative;font-family:"Lato",sans-serif}
  .panel-label{position:absolute;font-family:"Lato",sans-serif;font-size:24px;color:#2a2a2a;font-weight:400}
  .card{position:absolute;width:542px;height:303px;background:var(--card);border:1px solid var(--card-edge);overflow:hidden}
  .person{position:absolute;left:40px;top:58px}
  .person-name{font-weight:700;font-size:17px;color:var(--navy);letter-spacing:.3px}
  .person-role{font-size:14.5px;color:var(--navy);margin-top:3px}
  .brand{position:absolute;left:338px;top:30px;color:var(--brand-grey);font-weight:300;display:flex;align-items:center;gap:10px}
  .brand-name{font-size:46px;line-height:1;letter-spacing:-1px}
  .brand-sub{font-size:13px;letter-spacing:2px;margin-top:2px;text-align:center}
  .brand-mark{width:22px;height:22px;background:var(--brand-grey)}
  .photo-frame{position:absolute;left:42px;top:114px;width:100px;height:122px;border:5px solid;border-image:linear-gradient(#9fd0ea,#1d3b53) 1;display:flex;align-items:center;justify-content:center}
  .photo-slot{position:absolute;inset:0;background:linear-gradient(#ffffff,#f3f6f9)}
  .photo-text{position:relative;font-weight:700;font-size:20px;color:#6d8698}
  .contacts{position:absolute;left:172px;top:153px;list-style:none}
  .contacts li{display:flex;align-items:center;gap:12px;height:23.5px;font-size:16px;color:var(--ink)}
  .contacts li.strong{font-weight:700}
  .contacts svg{width:14px;height:14px;flex:none}
  .band{position:absolute;left:0;bottom:0;width:100%;height:46px}
  .band svg{position:absolute;inset:0;width:100%;height:100%}
  .band-url{position:absolute;bottom:12px;font-family:"Roboto Condensed",sans-serif;font-weight:700;font-size:13px;color:#fff;letter-spacing:.3px}
  .band-url.left{left:40px}
  .band-url.right{right:40px}
  .info{position:absolute;left:41px;top:73px;list-style:none;font-size:15.5px;color:var(--muted);font-weight:400}
  .info li{height:25.2px}
  .social{position:absolute;left:398px;top:53px;display:flex;gap:4px}
  .social span{width:40px;height:40px;border-radius:6px;background:#6f8da3}
  .write-lines{position:absolute;left:41px;top:62px;width:450px}
  .write-lines span{display:block;height:1.5px;background:var(--line);margin-bottom:40px}
</style>
</head>
<body>
  <span class="panel-label" style="left:51px;top:10px">Front</span>
  <span class="panel-label" style="left:609px;top:9px">Back</span>
  <span class="panel-label" style="left:56px;top:370px">Inside</span>

  <svg width="0" height="0" style="position:absolute">
    <defs>
      <linearGradient id="band-dark" x1="0" y1="0" x2="1" y2="0">
        <stop offset="0" stop-color="#0c1f2b"/><stop offset=".6" stop-color="#163545"/><stop offset="1" stop-color="#0c1f2b"/>
      </linearGradient>
      <linearGradient id="band-glow" x1="0" y1="0" x2="0" y2="1">
        <stop offset="0" stop-color="#1f4456" stop-opacity="0"/><stop offset="1" stop-color="#2c5d73" stop-opacity=".8"/>
      </linearGradient>
      <linearGradient id="band-strip" x1="0" y1="0" x2="1" y2="0">
        <stop offset="0" stop-color="#dff1fa"/><stop offset=".45" stop-color="#9fd0ea"/><stop offset="1" stop-color="#1f4456"/>
      </linearGradient>
      <symbol id="band-shape" viewBox="0 0 542 46" preserveAspectRatio="none">
        <polygon points="322,0 542,0 542,18 356,18" fill="url(#band-strip)"/>
        <polygon points="0,0 300,0 338,23 542,23 542,46 0,46" fill="url(#band-dark)"/>
        <rect x="0" y="28" width="542" height="18" fill="url(#band-glow)"/>
        <polyline points="307,0 345,21 542,21" fill="none" stroke="#ffffff" stroke-width="3"/>
      </symbol>
    </defs>
  </svg>

  <!-- Front -->
  <section class="card card-front" style="left:51px;top:48px">
    <div class="person">
      <p class="person-name">DANA WHITFORD</p>
      <p class="person-role">Managing Director/ Principal REA</p>
    </div>
    <div class="brand">
      <div><p class="brand-name">kestrel</p><p class="brand-sub">home services</p></div>
      <span class="brand-mark"></span>
    </div>
    <div class="photo-frame"><div class="photo-slot" role="img" aria-label="Portrait photo of the managing director"></div><span class="photo-text">Photo</span></div>
    <ul class="contacts">
      <li class="strong"><svg viewBox="0 0 14 14"><path d="M3 1.5l2 .2.8 2.6-1.3 1a6 6 0 003.6 3.6l1-1.3 2.6.8.2 2c-1 1-2 1.2-3 .9A9 9 0 012.1 4.5C1.8 3.5 2 2.5 3 1.5z" fill="#1d3b53"/></svg>1300 555 014</li>
      <li class="strong"><svg viewBox="0 0 14 14"><rect x="3.5" y="1" width="7" height="12" rx="1.2" fill="none" stroke="#1d3b53" stroke-width="1.4"/><rect x="5.5" y="10.5" width="3" height="1" fill="#1d3b53"/></svg>0400 555 218</li>
      <li><svg viewBox="0 0 14 14"><rect x="1" y="3" width="12" height="8" fill="none" stroke="#1d3b53" stroke-width="1.1"/><polyline points="1,3 7,8 13,3" fill="none" stroke="#1d3b53" stroke-width="1.1"/></svg>dana@kestrelhomeservices.com.au</li>
    </ul>
    <div class="band"><svg><use href="#band-shape"/></svg><span class="band-url left">WWW.KESTRELHOMESERVICES.COM.AU</span></div>
  </section>

  <!-- Back -->
  <section class="card card-back" style="left:608px;top:48px">
    <div class="person" style="top:55px">
      <p class="person-name">LEAH MARSH</p>
      <p class="person-role">Rental Manager</p>
    </div>
    <div class="brand">
      <div><p class="brand-name">kestrel</p><p class="brand-sub">home services</p></div>
      <span class="brand-mark"></span>
    </div>
    <div class="photo-frame" style="top:110px"><div class="photo-slot" role="img" aria-label="Portrait photo of the rental manager"></div><span class="photo-text">Photo</span></div>
    <ul class="contacts" style="top:150px">
      <li class="strong"><svg viewBox="0 0 14 14"><path d="M3 1.5l2 .2.8 2.6-1.3 1a6 6 0 003.6 3.6l1-1.3 2.6.8.2 2c-1 1-2 1.2-3 .9A9 9 0 012.1 4.5C1.8 3.5 2 2.5 3 1.5z" fill="#1d3b53"/></svg>1300 555 014</li>
      <li class="strong"><svg viewBox="0 0 14 14"><rect x="3.5" y="1" width="7" height="12" rx="1.2" fill="none" stroke="#1d3b53" stroke-width="1.4"/><rect x="5.5" y="10.5" width="3" height="1" fill="#1d3b53"/></svg>0400 555 731</li>
      <li><svg viewBox="0 0 14 14"><rect x="1" y="3" width="12" height="8" fill="none" stroke="#1d3b53" stroke-width="1.1"/><polyline points="1,3 7,8 13,3" fill="none" stroke="#1d3b53" stroke-width="1.1"/></svg>leah@kestrelhomeservices.com.au</li>
    </ul>
    <div class="band"><svg><use href="#band-shape"/></svg><span class="band-url left">WWW.KESTRELHOMESERVICES.COM.AU</span></div>
  </section>

  <!-- Inside left -->
  <section class="card card-inside" style="left:54px;top:408px">
    <div class="social"><span></span><span></span></div>
    <ul class="info">
      <li>Apply online: http://bit.ly/khsapp</li>
      <li>1300 OUR HOME</li>
      <li>ACN: 000 555 112</li>
      <li>Postal Address: PO Box 418, Seabrook Q 4999</li>
      <li>Office Location: Level 1/57 Harbour Parade, Seabrook Q 4999</li>
    </ul>
    <div class="band"><svg><use href="#band-shape"/></svg><span class="band-url left">WWW.KESTRELHOMESERVICES.COM.AU</span></div>
  </section>

  <!-- Inside right -->
  <section class="card card-notes" style="left:610px;top:408px">
    <div class="write-lines"><span></span><span></span><span></span><span></span></div>
    <div class="band"><svg style="transform:scaleX(-1)"><use href="#band-shape"/></svg><span class="band-url right">WWW.KESTRELHOMESERVICES.COM.AU</span></div>
  </section>
</body>
</html>
```